Glimmora Pages with Bold Font

I want the font to be simple yet bold for Glimmora images. Its all about a simple bold readable font. I need a single glimmora page with an image and copy/text on or over the image. The words will change in the future. I'm looking for the right font. I like fiery red and yellow colors. The "One Pic" attached is a sample of what I want without the Veltrix words.

```html
<!DOCTYPE html>
<html lang="en">
<head>
<meta charset="utf-8">
<title>Glimmora Page – Trainer For Men</title>
<link rel="stylesheet" href="https://fonts.googleapis.com/css2?family=Montserrat:wght@800;900&family=Oswald:wght@500;600&family=Bree+Serif&display=swap">
<style>
  :root {
    --fiery-red: #d21f26;
    --white: #ffffff;
    --photo-light: #d9d3cd;
    --photo-mid: #a38a7c;
    --photo-dark: #2a211d;
    --ink: #141010;
  }
  html, body {
    margin: 0;
    padding: 0;
    width: 1200px;
    height: 1200px;
    overflow: hidden;
    background: var(--ink);
  }
  .promo {
    position: relative;
    width: 1200px;
    height: 1200px;
    overflow: hidden;
  }
  .promo__photo {
    position: absolute;
    inset: 0;
    background:
      radial-gradient(ellipse 55% 70% at 62% 48%, #b89684 0%, rgba(163,138,124,0.6) 45%, rgba(163,138,124,0) 75%),
      linear-gradient(160deg, var(--photo-mid) 0%, var(--photo-light) 35%, #c4b8ae 55%, #6b5246 80%, var(--photo-dark) 100%);
  }
  .promo__shade {
    position: absolute;
    inset: 0;
    background: linear-gradient(180deg, rgba(0,0,0,0.25) 0%, rgba(0,0,0,0.05) 40%, rgba(0,0,0,0.35) 70%, rgba(0,0,0,0.75) 100%);
  }
  .brand {
    position: absolute;
    left: 61px;
    top: 30px;
    display: flex;
    align-items: flex-start;
    gap: 8px;
  }
  .brand__name {
    font-family: "Bree Serif", serif;
    font-size: 32px;
    color: var(--fiery-red);
    margin-top: 10px;
  }
  .brand__role {
    font-family: "Bree Serif", serif;
    font-size: 22px;
    color: var(--white);
  }
  .headline {
    position: absolute;
    left: 64px;
    top: 128px;
    margin: 0;
    font-family: "Montserrat", sans-serif;
    font-weight: 800;
    font-size: 70px;
    line-height: 74px;
    color: var(--white);
    letter-spacing: -0.5px;
  }
  .offer {
    position: absolute;
    left: 58px;
    top: 318px;
    margin: 0;
    font-family: "Montserrat", sans-serif;
    font-weight: 900;
    font-size: 166px;
    line-height: 142px;
    color: var(--white);
    letter-spacing: -3px;
  }
  .offer__line { display: block; }
  .accent { color: var(--fiery-red); }
  .offer__you {
    display: inline-block;
    padding-bottom: 8px;
    border-bottom: 7px solid var(--fiery-red);
    line-height: 118px;
    margin-top: 12px;
  }
  .body-copy {
    position: absolute;
    left: 62px;
    top: 872px;
    margin: 0;
    font-family: "Oswald", sans-serif;
    font-weight: 500;
    color: var(--white);
  }
  .body-copy__line {
    display: block;
    font-size: 40px;
    line-height: 66px;
    letter-spacing: -0.5px;
  }
  .body-copy__promise {
    display: block;
    font-weight: 600;
    font-size: 44px;
    line-height: 60px;
    color: var(--fiery-red);
    letter-spacing: -0.5px;
  }
</style>
</head>
<body>
  <main class="promo">
    <div class="promo__photo" role="img" aria-label="Close-up photograph of a woman's toned midriff in red lace lingerie with a belly chain, soft light background"></div>
    <div class="promo__shade"></div>

    <header class="brand">
      <span class="brand__name">Mara Quinn Vale</span>
      <span class="brand__role">Trainer For Men</span>
    </header>

    <h1 class="headline">Wanna lose weight?<br>Wanna shrink that gut?</h1>

    <p class="offer">
      <span class="offer__line"><span class="accent">I</span> CAN</span>
      <span class="offer__line">HELP</span>
      <span class="offer__line offer__you"><span class="accent">YOU</span>!</span>
    </p>

    <p class="body-copy">
      <span class="body-copy__line">The secret is to find what works for <span class="accent">YOU</span>!</span>
      <span class="body-copy__line">And I can give you that.</span>
      <span class="body-copy__promise">The pounds will melt away,</span>
      <span class="body-copy__promise">your gut will shrink, and your health will improve.</span>
    </p>
  </main>
</body>
</html>
```